Business card por a urban DJ, up scale audience target

Need a sober design, modern, conservative colors but i can consider some options, y play rnb, hip hop, EDM and top40.

Business card for contact and personal info, double sided, use logo attrached please; im 42 so i need a card acording to my age an target audience.

Target Market(s)

Adult people, up scale audience

Industry/Entity Type

Music Download

Contact Information for Business Card

Cel (318) 5024471963 www.kelvarodun.com

Requirements
Must have
• open mind
Nice to have
• open mind
Should not have
• DJ

```html
<!DOCTYPE html>
<html lang="en">
<head>
<meta charset="utf-8">
<title>Kelva — Business Card</title>
<link rel="stylesheet" href="https://fonts.googleapis.com/css2?family=Open+Sans:wght@600&display=swap">
<style>
  :root {
    --backdrop: #d4d4d4;
    --card: #2c2c2c;
    --seal: #000000;
    --ink: #ffffff;
  }
  html, body {
    margin: 0;
    padding: 0;
    width: 1200px;
    height: 1000px;
    overflow: hidden;
    background: var(--backdrop);
    font-family: "Open Sans", Arial, sans-serif;
  }
  .canvas {
    position: relative;
    width: 1200px;
    height: 1000px;
  }
  .card {
    position: absolute;
    background: var(--card);
    color: var(--ink);
  }
  .card--front { left: 152px; top: 155px; width: 399px; height: 665px; }
  .card--back  { left: 678px; top: 154px; width: 396px; height: 660px; }

  .seal {
    position: absolute;
    left: 70px;
    top: 187px;
    width: 254px;
    height: 254px;
    border-radius: 50%;
    background: var(--seal);
    display: flex;
    align-items: center;
    justify-content: center;
  }
  .brand-name {
    font-weight: 600;
    color: var(--ink);
    letter-spacing: 2px;
    line-height: 1;
  }
  .seal .brand-name { font-size: 54px; }

  .contact-list {
    position: absolute;
    left: 39px;
    top: 62px;
    margin: 0;
    padding: 0;
    list-style: none;
    font-size: 14px;
    letter-spacing: 0.3px;
  }
  .contact-item {
    display: flex;
    align-items: center;
    height: 30px;
  }
  .contact-icon {
    width: 18px;
    height: 18px;
    margin-right: 9px;
    flex: none;
  }
  .card--back .brand-name {
    position: absolute;
    right: 37px;
    bottom: 52px;
    font-size: 58px;
  }
</style>
</head>
<body>
<main class="canvas">
  <section class="card card--front" aria-label="Card front">
    <div class="seal">
      <span class="brand-name">KELVA</span>
    </div>
  </section>

  <section class="card card--back" aria-label="Card back">
    <ul class="contact-list">
      <li class="contact-item">
        <svg class="contact-icon" viewBox="0 0 18 18" aria-hidden="true">
          <rect x="5" y="1.5" width="8" height="15" rx="1.5" fill="none" stroke="#fff" stroke-width="1.4"/>
          <line x1="8" y1="14" x2="10" y2="14" stroke="#fff" stroke-width="1.2"/>
        </svg>
        <span>(318) 5024471963</span>
      </li>
      <li class="contact-item">
        <svg class="contact-icon" viewBox="0 0 18 18" aria-hidden="true">
          <g fill="none" stroke="#fff" stroke-width="1.2">
            <circle cx="9" cy="9" r="7.2"/>
            <ellipse cx="9" cy="9" rx="3.2" ry="7.2"/>
            <line x1="1.8" y1="9" x2="16.2" y2="9"/>
            <path d="M3 5.2h12M3 12.8h12"/>
          </g>
        </svg>
        <span>www.kelvarodun.com</span>
      </li>
    </ul>
    <span class="brand-name">KELVA</span>
  </section>
</main>
</body>
</html>
```